Web Design for Solar Energy Consultancy Company

~ May 3, 2017 Update ~
As our project is rapidly progressing towards its completion, we started building up the list of designs that attracted the most of the team's attention. Additional submittals are still most welcome. Before submitting your proposal, however, we can recommend to review the concepts that received 4 stars as these are the ones that, in our opinion, most closely match the brief's requirements. Thank you!!
~ April 30, 2017 Update ~
The project deadline has been extended to attract a broader design community and to better tailor the final design to the requirements of the project.
A "light", "clean" (minimalistic), professionally looking, unique design is expected. Please, try to avoid industry cliches. Also, please use green, which became another industry cliche, with great caution. The brief provides minimum details to foster creativity. With the same notion in mind, the page content information is not provided.
Thank you for your feedback and support of the project!!
~ April 22, 2017 Update ~
Additional comments after starting receiving more designs:
- your attention to the brief's requirements will be highly appreciated. It is expected that the design is unique - standard, commonly used, images, formats and approaches do not fall under this category. There is no need to "bombard" with slightly different variations of the same design. It is expected that a conceptual (preliminary) design is submitted first, and, after it is reviewed (each design will receive a star rating and, if the star rating is greater than 3, a detailed feedback), the requested changes are implemented. We believe this will allow to approach the design process more efficiently and safe additional time to both the Designers's Community and our company. Thank you for understanding.
Clarification, please submit two variations of a design:
1) 1 page "business card" design that the company will be able to use during its startup stage;
2) the fully functional design (as per the requirements outlined below) for the company to transition to after the start-up period is over. Same design principles as developed for option 1 should be used for this variation.
Additional clarification, please note that the news block will not require images (at least during the start-up stage). It is envisioned to be a news feeder.
~ April 21, 2017 Update ~
Preliminary comments after receiving first designs:
- please try to create a unique design, using common elements wisely. Though such solar energy "attributes" as a solar panel or a bulb are very well recognized and allow quickly identify the nature of the business, they also became so common that in many cases a design may seem very similar to the one of others (Oh!, I've already seen this... effect).
- please try to introduce the company's logo unobtrusively. The size and position of the logo should clearly identify the company, but the message should be subtle, the logo should not distract from the main design. Brevam's swoosh did not need to occupy have the screen.
- please use the green color with caution as it was with the company's logo. True, it is a green energy. But there is no need for the color to "scream" about it. Use the amount of green and its tone (avoid acid green) wisely.
--------------------------------------------------------------------------------
1. Main Goal
Develop a website that can represent the company to the industry stakeholders and become its "business card" during the start-up stage.
2. Secondary Goal
Develop a structure of a fully functional website that the "business card" design can eventually be transformed to staying consistent with the original design principles.
3. Key Audience
Varlo Corp. is providing consulting and technical services in the area of Solar Energy. The industry stakeholders include project developers, financial community, governmental bodies, OEMs, and competition.
4. Site Map
- HOME
• About
• Services
• Solar Energy
• News
• Contacts
• Social Media
- SERVICES*
- PROJECTS*
- FINANCE*
- TRAINING*
- SOLAR (ENERGY)*
* Maybe inactive / partially functional during the start-up stage.
5. Technical Specifications
Online brochure website during the start-up stage with a capability to be eventually transformed to a fully functional website while preserving the original design principles.
The design to be appealing, "light", professional, and with an intuitive and easy to navigate interface. Modern coding principles supporting efficiency and security to be utilized. Newest industry trends in website coding will be welcome.
The website to be designed so that it would fit well a computer, tablet, or mobile phone screen of any size. Cross-platform functionality to be taken into consideration to ensure that the website is fully functional on any platform.
Company's logo has already been designed and will be shared with the short-listed designers during the final design stage.
6. Interaction
The website will provide information about the company, our services, and projects. In addition, the industry insight, accumulated knowledge, and most recent trends are planned to be shared with stakeholders and attract and retain the audience.
Interaction with designers during the website development is envisioned to go through the following steps:
a) conceptual design - to be proposed by a designer originally. All conceptual designs will be reviewed and a feedback provided to pre-selected designers;
b) (preliminary and) final design - depending on the level of additional changes required can be broken into two steps. After discussing preliminary designs, company images will be provided to the selected finalists, who will compete with their final proposals.
7. Industry Stakeholders
- https://www.quelbrant.example/power/solar-power.- http://www.tavlorpeak.example/
- http://www.morvexaworks.example/about/company/
- https://www.pyxbel.example/energy/index.html
8. Budget
Defined by the project.
9. Timescale
Defined by the project.
12. Additional Info
- No copy-cats, standard graphics, or cliches please!
- Additional information / clarifications will be gladly provided upon request.
- This specification may be updated throughout the project to reflect discussions with / changes proposed by the Designers community.
Updates

```html
<!DOCTYPE html>
<html lang="en">
<head>
<meta charset="utf-8">
<title>Varlo Corp – Solar Energy Consulting</title>
<link rel="stylesheet" href="https://fonts.googleapis.com/css2?family=Exo+2:wght@600;700&family=Lato:ital,wght@0,400;0,700;1,400&display=swap">
<style>
:root{
  --green:#3fa535;
  --green-dark:#2a8a24;
  --yellow:#f5b400;
  --orange:#f39200;
  --ink:#1d1d1d;
  --text:#444;
  --muted:#777;
  --grey-bg:#efefef;
  --line:#d9d9d9;
  --footer:#0b0b0b;
  --white:#fff;
}
*{box-sizing:border-box;margin:0;padding:0}
html,body{width:1200px;height:2946px;overflow:hidden}
body{position:relative;background:var(--white);font-family:"Lato",sans-serif;color:var(--text);font-size:12px;line-height:1.75}
.abs{position:absolute}
.heading{font-family:"Exo 2",sans-serif;font-weight:700;color:var(--ink);font-size:27px;line-height:1.2}
.heading em{font-style:normal;color:var(--green)}
.rule{display:flex;align-items:center}
.rule::before{content:"";width:12px;height:12px;border-radius:50%;background:#bbb;margin-right:4px}
.rule::after{content:"";flex:1;height:1px;background:var(--line)}
.btn{display:inline-flex;align-items:center;justify-content:space-between;height:32px;border-radius:16px;padding:0 4px 0 18px;font-weight:700;font-size:12px;color:var(--white);text-transform:uppercase}
.btn .arrow{width:26px;height:26px;border-radius:50%;background:var(--white);display:flex;align-items:center;justify-content:center;margin-left:12px}
.btn.green{background:linear-gradient(#4cb43f,#2a8a24)}
.btn.yellow{background:linear-gradient(#ffc21a,#eea600);color:var(--ink)}
.pager{display:flex;gap:4px}
.pager span{width:24px;height:24px;display:flex;align-items:center;justify-content:center;background:#ddd}
.pager span.on{background:var(--green)}

/* header */
.header{top:0;left:0;width:1200px;height:110px;background:linear-gradient(#fff,#f1f1f1)}
.brand{left:161px;top:36px;display:flex;align-items:center;gap:10px}
.brand .mark{width:46px;height:46px;border-radius:50%;background:var(--yellow)}
.brand .name{font-weight:700;font-size:30px;color:#333;letter-spacing:1px}
.topbar{top:0;left:590px;height:37px;display:flex}
.topbar .phone{width:186px;background:var(--green);color:var(--white);font-size:16px;display:flex;align-items:center;justify-content:center;gap:10px}
.topbar .consult{width:261px;background:var(--yellow);color:var(--white);font-weight:700;font-size:14px;display:flex;align-items:center;justify-content:center;gap:10px;text-transform:uppercase}
.nav{top:76px;left:496px;display:flex;font-size:13px;color:#333}
.nav a{color:inherit;text-decoration:none;padding:0 20px;border-left:1px solid #ccc}
.nav a:first-child{border:none;color:var(--green);font-weight:700;border-bottom:2px solid var(--green)}

/* hero */
.hero{top:110px;left:0;width:1200px;height:522px;background:linear-gradient(175deg,#c9cfc4 0%,#9aa78a 14%,#6f7f5c 24%,#8b8f8e 34%,#6e757e 55%,#4c535d 75%,#6f7680 100%)}
.hero-bubble{left:157px;top:216px;width:314px;height:314px;border-radius:50%;background:rgba(60,60,60,.62);color:var(--white);text-align:center;padding-top:70px}
.hero-bubble p{font-family:"Exo 2",sans-serif;font-weight:700;font-size:19px;line-height:1.35;text-transform:uppercase;padding:0 40px}
.hero-bubble .btn{margin-top:16px}
.dots{top:596px;left:560px;display:flex;gap:6px}
.dots i{width:8px;height:8px;border-radius:50%;background:#ddd;display:block}
.dots i.on{background:var(--yellow)}

/* services */
.services{top:632px;left:0;width:1200px;height:528px}
.services .heading{left:161px;top:47px}
.services .rule{left:161px;top:94px;width:520px}
.services .pager{left:679px;top:85px}
.services .intro{left:161px;top:114px;width:576px;font-size:11px;line-height:1.6}
.card{top:163px;width:279px}
.card .photo{height:152px}
.card h3{font-family:"Exo 2",sans-serif;font-size:18px;color:var(--ink);margin:12px 0 6px}
.card p{font-size:11px;line-height:1.75}
.card .btn{margin-top:14px}
.form{left:772px;top:53px;width:267px;height:421px;background:var(--white);box-shadow:0 3px 10px rgba(0,0,0,.2)}
.form .top{height:46px;background:linear-gradient(#4cb43f,#2a8a24);color:var(--white);font-family:"Exo 2",sans-serif;font-weight:700;font-size:17px;display:flex;align-items:center;justify-content:center;text-transform:uppercase}
.form .inner{padding:14px 18px}
.form h4{font-size:14px;color:#333;font-weight:700}
.form .sub{font-size:11px;color:var(--muted);line-height:1.5;margin:10px 0 18px}
.form .field{height:33px;border:1px solid #ddd;background:#f7f7f7;margin-bottom:6px;padding:8px;font-size:10px;font-style:italic;color:#999;line-height:1.2}
.form .field.area{height:72px}
.form .btn{margin-top:8px}

/* about */
.about{top:1160px;left:0;width:1200px;height:376px;background:var(--grey-bg);text-align:center}
.about .heading{margin-top:42px}
.about .rule{width:180px;margin:14px auto 16px}
.about .lead{font-weight:700;color:#222;font-size:13px}
.about p{width:880px;margin:8px auto 0;font-size:11.5px;line-height:2.05}
.about .btn{margin-top:22px}

/* projects */
.projects{top:1536px;left:0;width:1200px;height:738px;text-align:center}
.projects .heading{margin-top:46px}
.projects .rule{width:180px;margin:14px auto 12px}
.projects .intro{font-size:11.5px;line-height:1.65}
.tile{overflow:hidden}
.tile.feature{background:linear-gradient(#3a4540,#1c2a33 60%,#26303a)}
.tile.feature .overlay{position:absolute;inset:0;background:rgba(0,0,0,.45);color:var(--white);padding:62px 40px 0;text-align:center}
.tile.feature h3{font-family:"Exo 2",sans-serif;font-size:21px;color:var(--yellow);text-transform:uppercase}
.tile.feature p{font-size:11.5px;line-height:1.65;margin-top:6px}
.tile.feature .plus{width:26px;height:26px;border:2px solid var(--yellow);border-radius:50%;margin:12px auto 0;display:flex;align-items:center;justify-content:center}

/* news & testimonials */
.lower{top:2274px;left:0;width:1200px;height:330px;background:var(--grey-bg)}
.col-head{top:48px}
.news{left:161px;width:406px}
.testi{left:633px;width:406px}
.col-head .pager{position:absolute;right:0;top:8px}
.col-head .pager span{width:20px;height:20px}
.col-head .rule{margin-top:8px}
.item{display:flex;gap:18px;margin-top:20px;padding-bottom:16px;border-bottom:1px solid #d6d6d6}
.item:last-child{border:none}
.date{width:36px;flex:none;text-align:center;border:1px solid #ccc;background:var(--white);align-self:flex-start}
.date b{display:block;font-size:14px;color:#222;line-height:28px}
.date span{display:block;background:var(--green);color:var(--white);font-size:9px;font-weight:700;line-height:16px}
.item h4{font-size:13px;color:#222;line-height:1.3}
.item p{font-size:11.5px;line-height:1.5;margin-top:2px}
.quote{display:flex;gap:22px;margin-top:20px}
.avatar-wrap{flex:none;text-align:center;width:86px}
.avatar{width:84px;height:84px;border-radius:50%;border:4px solid var(--green);background:linear-gradient(#f2f2f2,#c9c2ba)}
.avatar-wrap span{display:block;font-size:11px;color:var(--green);font-weight:700;margin-top:4px}
.quote p{font-style:italic;font-size:11.5px;line-height:1.75}
.divider{top:2330px;left:599px;width:1px;height:210px;background:#d6d6d6}

/* footer */
.footer-shape{top:2560px;left:0;width:1200px;height:347px}
.footer-logo{top:2556px;left:568px;width:64px;height:64px;border-radius:50%;background:var(--white);border:3px solid var(--orange);display:flex;align-items:center;justify-content:center}
.footer-logo i{width:40px;height:40px;border-radius:50%;background:var(--yellow);display:block}
.fcol{top:2673px;color:#ddd;font-size:11.5px}
.fcol h5{font-family:"Exo 2",sans-serif;font-size:16px;color:var(--white);font-weight:700;padding-bottom:8px;border-bottom:1px solid #333;margin-bottom:10px}
.links li{list-style:none;line-height:26px;padding-left:12px;position:relative}
.links li::before{content:"›";position:absolute;left:0;color:var(--orange)}
.contact-row{display:flex;gap:10px;margin-bottom:14px;line-height:1.5}
.contact-row b{color:var(--yellow)}
.map{width:214px;height:116px;background:linear-gradient(135deg,#e6e2d3 0%,#cfe0c3 45%,#a9c9e4 100%);border:3px solid var(--white)}
.social li{list-style:none;display:flex;align-items:center;gap:10px;line-height:33px}
.social li i{width:16px;height:16px;background:var(--white);border-radius:2px;display:block}
.copyright{top:2907px;left:0;width:1200px;height:39px;background:var(--green-dark);color:var(--white);font-size:11px;display:flex;align-items:center;justify-content:center}
</style>
</head>
<body>

<header class="abs header">
  <div class="abs brand"><span class="mark"></span><span class="name">VARLO CORP</span></div>
  <div class="abs topbar">
    <div class="phone">
      <svg width="20" height="20" viewBox="0 0 20 20"><circle cx="10" cy="10" r="9" fill="none" stroke="#fff" stroke-width="1.5"/><path d="M7 5l2 2-1 1.5c.6 1.3 1.6 2.3 2.9 2.9L12.4 10l2 2-1.3 1.6C9.5 13.4 6.6 10.5 6.4 6.9z" fill="#fff"/></svg>
      +012 555 0199
    </div>
    <div class="consult">
      <svg width="22" height="18" viewBox="0 0 22 18"><path d="M2 2h13v9H7l-4 3v-3H2z" fill="#fff"/><path d="M16 6h4v8h-1v3l-3-3h-6v-2h6z" fill="#fff"/></svg>
      Get a free consultation
    </div>
  </div>
  <nav class="abs nav"><a>Home</a><a>About Us</a><a>Our Services</a><a>Solar Energy</a><a>News</a><a>Contacts Us</a></nav>
</header>

<section class="abs hero" role="img" aria-label="Two engineers in hard hats reviewing a tablet on a rooftop solar panel array, green hills behind"></section>
<div class="abs hero-bubble">
  <p>We are providing consulting and technical services in the area of solar energy</p>
  <span class="btn yellow">Learn more<span class="arrow"><svg width="10" height="10" viewBox="0 0 10 10"><path d="M3 1l4 4-4 4" stroke="#333" stroke-width="2" fill="none"/></svg></span></span>
</div>
<div class="abs dots"><i class="on"></i><i></i><i></i><i></i></div>

<section class="abs services">
  <h2 class="abs heading">Our <em>Services</em></h2>
  <div class="abs rule"></div>
  <div class="abs pager"><span><svg width="8" height="10"><path d="M6 1L2 5l4 4" stroke="#555" stroke-width="2" fill="none"/></svg></span><span class="on"><svg width="8" height="10"><path d="M2 1l4 4-4 4" stroke="#fff" stroke-width="2" fill="none"/></svg></span></div>
  <p class="abs intro">Lorem ipsum dolor sit amet, consectetuer adipiscing el it,tuer adipiscing el it,tuer adipiscing el it, sed diam nonummy nibh euismod tincid unt ut laoreet dolore magna aliquam erat volutpat.</p>

  <article class="abs card" style="left:161px">
    <div class="photo" role="img" aria-label="Consultants in hard hats reviewing plans outdoors" style="background:linear-gradient(#dfe8f0 0%,#b9c4c9 35%,#7d7a62 70%,#5e5a48 100%)"></div>
    <h3>Consulting Services</h3>
    <p>Lorem ipsum dolor sit amet, consectetuer adipiscing el it, sed diam nonummy nibh euismod tincidunt ut laoreet dolore magna aliquam erat volutpat.</p>
    <span class="btn green">Read more<span class="arrow"><svg width="10" height="10"><path d="M3 1l4 4-4 4" stroke="#333" stroke-width="2" fill="none"/></svg></span></span>
  </article>
  <article class="abs card" style="left:458px">
    <div class="photo" role="img" aria-label="Technicians in safety vests installing solar panels on a roof" style="background:linear-gradient(#8fb4dc 0%,#c3d3e2 30%,#51698f 55%,#3b4f75 80%,#8a9a4a 100%)"></div>
    <h3>Technical Services</h3>
    <p>Lorem ipsum dolor sit amet, consectetuer adipiscing el it, sed diam nonummy nibh euismod tincidunt ut laoreet dolore magna aliquam erat volutpat.</p>
    <span class="btn green">Read more<span class="arrow"><svg width="10" height="10"><path d="M3 1l4 4-4 4" stroke="#333" stroke-width="2" fill="none"/></svg></span></span>
  </article>

  <aside class="abs form">
    <div class="top">Get a free consultation</div>
    <div class="inner">
      <h4>Leave a Message</h4>
      <p class="sub">Lorem ipsum dolor sit amet, consectetuer adipiscing elit.</p>
      <div class="field">Name *</div>
      <div class="field">Phone *</div>
      <div class="field">Email *</div>
      <div class="field area">Message</div>
      <span class="btn yellow">Submit<span class="arrow"><svg width="10" height="10"><path d="M3 1l4 4-4 4" stroke="#333" stroke-width="2" fill="none"/></svg></span></span>
    </div>
  </aside>
</section>

<section class="abs about">
  <h2 class="heading">About <em>Varlo corp</em></h2>
  <div class="rule"></div>
  <p class="lead">Lorem ipsum dolor sit amet, consectetuer adipiscing elit, sed diam nonummy nibh euismod tincidunt ut laoreet dolore magna aliquam</p>
  <p>Lorem ipsum dolor sit amet, consectetuer adipiscing elit, sed diam nonummy nibh euismod tincidunt ut laoreet dolore magna aliquam erat volutpat. Ut wisi enim ad minim veniam, quis nostrud exerci tation ullamcorper suscipit lobortis nisl ut aliquip ex ea commodo consequat. Duis autem vel eum iriure dolor in hendrerit in vulputate velit esse molestie consequat, vel illum dolore eu feugiat nulla facilisis at vero eros et accumsan.</p>
  <p>et iusto odio dignissim qui blandit praesent luptatum zzril delenit augue duis dolore te feugait nulla facilisi Lorem ipsum dolor sit amet, consectetuer adipiscing elit, sed diam nonummy nibh euismod tincidunt ut laoreet dolore magna aliquam erat volutpat.</p>
  <span class="btn yellow">Read more<span class="arrow"><svg width="10" height="10"><path d="M3 1l4 4-4 4" stroke="#333" stroke-width="2" fill="none"/></svg></span></span>
</section>

<section class="abs projects">
  <h2 class="heading">Our <em>Projects</em></h2>
  <div class="rule"></div>
  <p class="intro">et iusto odio dignissim qui blandit praesent luptatum zzril delenit augue duis dolore te feugait nulla facilisi<br>Lorem ipsum dolor sit amet, consectetuer adipiscing elit, sed diam nonum.</p>
</section>
<div class="abs tile feature" style="left:161px;top:1709px;width:434px;height:232px" role="img" aria-label="Rooftop solar installation at dusk">
  <div class="overlay">
    <h3>Lorem Corporation</h3>
    <p>Lorem Ipsum is simply dummy text of the printing and typesetting industry. Lorem Ipsum has been the industry's standard dummy…</p>
    <div class="plus"><svg width="12" height="12"><path d="M6 1v10M1 6h10" stroke="#f5b400" stroke-width="2"/></svg></div>
  </div>
</div>
<div class="abs tile" style="left:603px;top:1709px;width:434px;height:232px;background:linear-gradient(160deg,#b9c7b0 0%,#e6e9ec 25%,#3c5a86 50%,#d2d6da 70%,#5a6a4f 100%)" role="img" aria-label="Aerial view of a large rooftop solar array beside a road"></div>
<div class="abs tile" style="left:161px;top:1950px;width:228px;height:230px;background:linear-gradient(#c9d8e8 0%,#c58c45 18%,#7a8a4a 30%,#4f6ea6 50%,#23386a 100%)" role="img" aria-label="Solar panels in front of autumn trees"></div>
<div class="abs tile" style="left:399px;top:1950px;width:304px;height:230px;background:linear-gradient(#e4eaf1 0%,#9a8f7d 28%,#5b6f8f 50%,#2f456f 100%)" role="img" aria-label="Long rows of solar panels on a rooftop"></div>
<div class="abs tile" style="left:711px;top:1950px;width:326px;height:230px;background:linear-gradient(#e6eaee 0%,#c4cad1 38%,#3f5234 52%,#34425f 70%,#2a3550 100%)" role="img" aria-label="Ground-mounted solar farm under a cloudy sky"></div>
<div class="abs" style="left:540px;top:2203px"><span class="btn green">View all<span class="arrow"><svg width="10" height="10"><path d="M3 1l4 4-4 4" stroke="#333" stroke-width="2" fill="none"/></svg></span></span></div>

<section class="abs lower">
  <div class="abs col-head news">
    <h2 class="heading">Latest <em>News</em></h2>
    <div class="pager"><span><svg width="8" height="10"><path d="M6 1L2 5l4 4" stroke="#555" stroke-width="2" fill="none"/></svg></span><span class="on"><svg width="8" height="10"><path d="M2 1l4 4-4 4" stroke="#fff" stroke-width="2" fill="none"/></svg></span></div>
    <div class="rule"></div>
    <div class="item"><div class="date"><b>08</b><span>FEB</span></div><div><h4>Sed ut perspiciatis unde omnis iste natus error sit</h4><p>Accus doloremque laudantium, totamrem aperiam, moreliol mokriml eaquemi ipsa quae ab illoi facilies.</p></div></div>
    <div class="item"><div class="date"><b>08</b><span>FEB</span></div><div><h4>Sed ut perspiciatis unde omnis iste natus error sit</h4><p>Accus doloremque laudantium, totamrem aperiam, moreliol mokriml eaquemi ipsa quae ab illoi facilies.</p></div></div>
  </div>
  <div class="abs col-head testi">
    <h2 class="heading">Client <em>Testimonials</em></h2>
    <div class="pager"><span><svg width="8" height="10"><path d="M6 1L2 5l4 4" stroke="#555" stroke-width="2" fill="none"/></svg></span><span class="on"><svg width="8" height="10"><path d="M2 1l4 4-4 4" stroke="#fff" stroke-width="2" fill="none"/></svg></span></div>
    <div class="rule"></div>
    <div class="quote">
      <div class="avatar-wrap"><div class="avatar" role="img" aria-label="Client portrait"></div><span>- Mark Elden</span></div>
      <p>“Lorem ipsum sit amet co adipisclitsed udmim eisli mol monk dtepr incidiunt ut la dolore mabonk aliquammi kn nibhmi enim nim veni exercitationhmi enim nim veni exercit ationnom ullamco ips sdlitnol am conajdk adipiscig elitsedmik do eiusmod te epo uam acculi dollarmjk orenquem laudantium morelik.”</p>
    </div>
  </div>
</section>
<div class="abs divider"></div>

<svg class="abs footer-shape" viewBox="0 0 1200 347" preserveAspectRatio="none">
  <rect width="1200" height="347" fill="#efefef"/>
  <path d="M0 120 Q600 -20 1200 120 V347 H0Z" fill="#0b0b0b"/>
  <path d="M0 120 Q600 -20 1200 120" fill="none" stroke="#f39200" stroke-width="5"/>
</svg>
<div class="abs footer-logo"><i></i></div>

<div class="abs fcol" style="left:161px;width:140px">
  <h5>Quick Links</h5>
  <ul class="links"><li>Home</li><li>About Us</li><li>Our Services</li><li>Solar Energy</li><li>News</li><li>Contact Us</li></ul>
</div>
<div class="abs fcol" style="left:346px;width:220px">
  <h5>Contact Details</h5>
  <div class="contact-row"><svg width="12" height="16" viewBox="0 0 12 16"><path d="M6 0a6 6 0 0 1 6 6c0 4-6 10-6 10S0 10 0 6a6 6 0 0 1 6-6z" fill="#f5b400"/><circle cx="6" cy="6" r="2" fill="#0b0b0b"/></svg><div><b>VARLO CORP</b><br>laoreetmok laoreet dol magnak<br>aliquam PG Feugait.</div></div>
  <div class="contact-row"><svg width="14" height="14" viewBox="0 0 20 20"><path d="M5 2l4 4-2 2.5c1 2 2.5 3.5 4.5 4.5L14 11l4 4-2.5 2.5C9 17 3 11 2.5 4.5z" fill="#f5b400"/></svg><div>123 - 555 - 0148</div></div>
  <div class="contact-row"><svg width="14" height="12" viewBox="0 0 14 10"><rect width="14" height="10" fill="#f5b400"/><path d="M0 0l7 5 7-5" stroke="#0b0b0b" fill="none"/></svg><div>info@varlocorp.example</div></div>
</div>
<div class="abs fcol" style="left:622px;width:214px">
  <h5>Location Map</h5>
  <div class="map" role="img" aria-label="Street map showing the office location"></div>
</div>
<div class="abs fcol" style="left:930px;width:107px">
  <h5>Follow Us</h5>
  <ul class="social"><li><i></i>Pagebook</li><li><i></i>Chirper</li><li><i></i>Circlenet</li><li><i></i>Worknet</li></ul>
</div>

<div class="abs copyright">copyright © 2016 Varlo solar consulting. All Rights Reserved</div>

</body>
</html>
```